redesign existing business card

Re design our business cards. We want a modern elegant design, open to ideas front side must contain similar details in a fresh look and style, back side we are open to suggestions. MUST USE COMPANY COLORS, WE WANT BRANDING. Need more ideas see www.brightstoneyards.com - Project must be done in one of adobe products and all files and fonts must be submitted to us. THIS IS A MUST

Target Market(s)

home owners

Industry/Entity Type

Construction Company

Contact Information for Business Card

see existing card file for information

Font styles to use
Sans Serif

Colors
0455a3
3377b5
34a6d7
0592cd
85cae6
ffffff

Requirements
Must have
• company colors, logo, contact info this is all for front side. back side be creative.

```html
<!DOCTYPE html>
<html lang="en">
<head>
<meta charset="utf-8">
<title>Brightstone Yards – Business Cards</title>
<link rel="stylesheet" href="https://fonts.googleapis.com/css2?family=Lato:wght@400;700&family=Alegreya:wght@400;700&display=swap">
<style>
  :root {
    --brand-deep: #0455a3;
    --brand-mid: #3377b5;
    --brand-sky: #34a6d7;
    --brand-bright: #0592cd;
    --brand-pale: #85cae6;
    --white: #ffffff;
    --card-black: #050505;
    --page-bg: #eceae6;
    --photo-dark: #1c2226;
    --photo-mid: #3a4348;
    --text-soft: #e8e8e8;
  }
  * { margin: 0; padding: 0; box-sizing: border-box; }
  html, body {
    width: 1200px; height: 900px; overflow: hidden;
    background: var(--page-bg);
  }
  .sheet {
    position: relative; width: 1200px; height: 900px;
    display: flex; align-items: center; justify-content: center; gap: 24px;
  }
  .card {
    position: relative; width: 560px; height: 320px; overflow: hidden;
    box-shadow: 0 6px 18px rgba(0,0,0,.18);
  }

  /* Back card – services over photo */
  .card--services { background: var(--photo-dark); font-family: "Lato", sans-serif; color: var(--text-soft); }
  .card__photo {
    position: absolute; inset: 0;
    background:
      linear-gradient(90deg, rgba(20,24,27,.92) 0%, rgba(20,24,27,.6) 55%, rgba(20,24,27,.45) 100%),
      radial-gradient(ellipse at 55% 70%, #2f4a5c 0%, transparent 45%),
      linear-gradient(180deg, var(--photo-mid) 0%, #2a3236 45%, #3c4347 100%);
  }
  .services {
    position: absolute; left: 44px; top: 62px;
    list-style: none; font-size: 15.5px; line-height: 19px; letter-spacing: .2px;
  }
  .tagline-family {
    position: absolute; left: 84px; top: 188px;
    color: var(--brand-sky); font-size: 15.5px;
  }
  .licence {
    position: absolute; left: 96px; top: 236px;
    font-size: 14px; line-height: 17px;
  }

  /* Brand name lockup (text only) */
  .brand {
    position: absolute; display: flex; align-items: center; gap: 8px;
    font-family: "Lato", sans-serif; font-weight: 700; color: var(--brand-sky);
    letter-spacing: .5px; text-transform: uppercase;
  }
  .brand__mark { width: 12px; height: 12px; background: var(--brand-bright); }
  .card--services .brand { right: 40px; top: 100px; font-size: 15px; }

  /* Front card – contact */
  .card--contact { background: var(--card-black); font-family: "Alegreya", serif; color: var(--white); }
  .card--contact .brand { right: 40px; top: 90px; font-size: 17px; }
  .person {
    position: absolute; left: 58px; top: 198px;
    color: var(--brand-mid); font-size: 27px; font-weight: 400;
  }
  .contact {
    position: absolute; left: 58px; top: 240px;
    font-size: 14px; line-height: 19px;
  }
  .contact__label { color: var(--brand-bright); }
  .contact__web { color: var(--brand-bright); }
</style>
</head>
<body>
<main class="sheet">
  <section class="card card--services">
    <div class="card__photo" role="img" aria-label="Dusk photo of a paved pool deck with palm trees and lounge chairs"></div>
    <ul class="services">
      <li>Driveway Pool Renovation Custom</li>
      <li>Out-Doorkitchhen</li>
      <li>Retaining Wall</li>
      <li>Paver Restoration</li>
      <li>H.O.A Project</li>
      <li>Patios &amp; Much More</li>
    </ul>
    <p class="tagline-family">Family Owned &amp; Operated</p>
    <p class="licence">License &amp; Insured<br>BRW 21 pv-40317-k PLM BCH u-5530<br>MARTIN MCPBT7718</p>
    <div class="brand"><span class="brand__mark"></span>Brightstone Yards</div>
  </section>

  <section class="card card--contact">
    <div class="brand"><span class="brand__mark"></span>Brightstone Yards</div>
    <h1 class="person">Marco Ellison</h1>
    <p class="contact">
      2150 N Harbor Ln suite 8 Delray Shores,FL 33401<br>
      <span class="contact__label">T:</span> (044) 555 010 200 <span class="contact__label">T:</span> (044) 555010201 <span class="contact__label">F:</span> (561)555-0147<br>
      <span class="contact__label">E:</span> marco@brightstoneyards.com <span class="contact__web">www.brightstoneyards.com</span>
    </p>
  </section>
</main>
</body>
</html>
```